Discreet simple classy for adult entertainment

I would like a matte black business card with gold writing for my business. Keeping it simple. Having my following:

Lina frost
Events. Entertainment. Promotions
0477250618

or alternatively could have what i had on my previous card below but i think i prefer the above as again - discretion.

Maybe a nice gold line thru the card or some other very simple design . Or not open to ideas/ can be doublesided if any good ideas with that.

included pics of my old bus card. not sure weather i want a photo on it or not. if i do it wont be the same pic. i kinda wanted a card that was discreet so if it was in someones wallet they wouldn't neccessarily realise it was from a stripper.

Target Market(s)

men

Industry/Entity Type

Business

Contact Information for Business Card

Lina frost
0477250618

Requirements
Nice to have
• i don't know i am really open to anything. im giving my cards to guys so something they can have in their wallet that is discreet preferably.

```html
<!DOCTYPE html>
<html lang="en">
<head>
<meta charset="utf-8">
<title>Lina Frost – Business Card</title>
<link href="https://fonts.googleapis.com/css2?family=Antonio:wght@100;200&display=swap" rel="stylesheet">
<style>
  :root {
    --page: #3b3b3b;
    --card: #000000;
    --gold: #cfa959;
    --gold-soft: #b8954f;
    --skin: #6a4a3a;
    --foliage: #243320;
    --water: #0f3a40;
    --float: #7a3c52;
  }
  * { margin: 0; padding: 0; box-sizing: border-box; }
  html, body {
    width: 1200px; height: 1200px; overflow: hidden;
    background: var(--page);
  }
  .canvas { position: relative; width: 1200px; height: 1200px; }
  .card {
    position: absolute; left: 296px; width: 608px; height: 346px;
    background: var(--card); overflow: hidden;
    font-family: "Antonio", "Arial Narrow", sans-serif;
    color: var(--gold);
  }
  .card--front { top: 232px; }
  .card--back  { top: 622px; }

  .card__photo { position: absolute; top: 0; height: 100%; }
  .card--front .card__photo {
    left: 0; width: 420px;
    background:
      linear-gradient(90deg, rgba(0,0,0,0) 0%, rgba(0,0,0,0) 55%, #000 100%),
      radial-gradient(ellipse at 42% 55%, var(--skin) 0%, #3a2a22 40%, rgba(0,0,0,0) 75%),
      linear-gradient(160deg, var(--foliage) 0%, #151a12 50%, #0a0a0a 100%);
  }
  .card--back .card__photo {
    left: 180px; right: 0;
    background:
      linear-gradient(90deg, #000 0%, rgba(0,0,0,0) 35%),
      radial-gradient(ellipse at 70% 45%, var(--skin) 0%, rgba(106,74,58,0.4) 25%, rgba(0,0,0,0) 50%),
      radial-gradient(ellipse at 55% 85%, var(--float) 0%, rgba(122,60,82,0.5) 35%, rgba(0,0,0,0) 65%),
      linear-gradient(180deg, var(--water) 0%, #0b2a30 60%, #081c20 100%);
  }

  .card__name {
    position: absolute; top: 22px; right: 29px;
    font-weight: 100; font-size: 64px; line-height: 1;
    letter-spacing: 14px; margin-right: -14px;
    text-transform: uppercase; white-space: nowrap;
  }
  .card__services {
    position: absolute; top: 196px; right: 33px;
    list-style: none; text-align: right;
    font-weight: 200; font-size: 16px; line-height: 20.5px;
    letter-spacing: 3.4px; text-transform: uppercase;
    color: var(--gold-soft); white-space: nowrap;
  }
  .card__phone {
    position: absolute; top: 280px; right: 29px;
    font-weight: 100; font-size: 46px; line-height: 1;
    letter-spacing: 6px; margin-right: -6px; white-space: nowrap;
  }
  .card__handle {
    position: absolute; left: 40px; top: 272px;
    display: flex; align-items: center; gap: 8px;
    font-weight: 200; font-size: 22px; letter-spacing: 2px;
  }
  .card__handle-mark { width: 14px; height: 14px; background: var(--gold); }
</style>
</head>
<body>
<main class="canvas">
  <section class="card card--front">
    <div class="card__photo" role="img" aria-label="Portrait photo of the entertainer among night foliage"></div>
    <h1 class="card__name">Lina Frost</h1>
    <ul class="card__services">
      <li>Events /</li>
      <li>Entertainment /</li>
      <li>Promotions /</li>
    </ul>
    <p class="card__phone">0477250618</p>
  </section>

  <section class="card card--back">
    <div class="card__photo" role="img" aria-label="Photo of the entertainer on a pink doughnut pool float over dark teal water"></div>
    <p class="card__handle"><span class="card__handle-mark"></span>@linafrost</p>
  </section>
</main>
</body>
</html>
```